Custom Label for Women's Supplement Brand

Need a product label for our products, we have a logo designed but need to incorporate it in to our product line which will have capsule bottles, tincture bottles, and eventually skin care. We originally wanted a label that had black as main color, but are open to options. Want it to be sleek, and pull the eye, simple yet fun. Even something different that doesn’t look like anyone else.
Updates

Low designer entries

Target Market(s)

Women 26-70

Requirements
Nice to have
• Would love some metallic accents

```html
<!DOCTYPE html>
<html lang="en">
<head>
<meta charset="utf-8">
<title>Multi Vitamine for Women – Label</title>
<link rel="stylesheet" href="https://fonts.googleapis.com/css2?family=Exo+2:wght@500;700;800&display=swap">
<style>
  :root {
    --page: #ffffff;
    --label-black: #141414;
    --label-black-soft: #222222;
    --panel-white: #f1f1f1;
    --edge-green: #7fb034;
    --brand-green: #6f9f2c;
    --title-white: #ffffff;
    --title-orange: #ec8a24;
    --metal-light: #f4f4f4;
    --metal-mid: #b9b9b9;
    --metal-dark: #6f6f6f;
    --pill-text: #1b1b1b;
    --band-blue: #3dbcd9;
    --band-blue-light: #62d3ea;
    --count-text: #111111;
  }
  html, body {
    margin: 0;
    padding: 0;
    overflow: hidden;
  }
  .canvas {
    position: relative;
    width: 1193px;
    height: 1200px;
    background: var(--page);
    overflow: hidden;
    font-family: "Exo 2", sans-serif;
  }
  .label {
    position: absolute;
    left: 140px;
    top: 125px;
    width: 913px;
    height: 950px;
    background: linear-gradient(180deg, var(--label-black-soft) 0%, var(--label-black) 60%);
    overflow: hidden;
  }
  .label-shapes {
    position: absolute;
    inset: 0;
  }
  .brand {
    position: absolute;
    left: 570px;
    top: 166px;
    width: 330px;
    display: flex;
    align-items: center;
    gap: 12px;
    color: var(--brand-green);
    font-weight: 500;
    font-size: 30px;
    line-height: 1;
  }
  .brand-dot {
    width: 18px;
    height: 18px;
    border-radius: 50%;
    background: var(--brand-green);
    flex: none;
  }
  .product-title {
    position: absolute;
    left: 206px;
    top: 398px;
    margin: 0;
    font-weight: 800;
    font-size: 112px;
    line-height: 82px;
    letter-spacing: 1px;
  }
  .product-title .line-multi { display: block; color: var(--title-white); }
  .product-title .line-vitamine { display: block; color: var(--title-orange); }
  .audience-pill {
    position: absolute;
    left: 208px;
    top: 593px;
    height: 64px;
    box-sizing: border-box;
    padding: 0 24px;
    display: flex;
    align-items: center;
    border-radius: 14px;
    background: linear-gradient(90deg, var(--metal-dark) 0%, var(--metal-light) 35%, var(--metal-mid) 70%, var(--metal-light) 100%);
    color: var(--pill-text);
    font-weight: 700;
    font-size: 38px;
  }
  .capsule-count {
    position: absolute;
    left: 56px;
    top: 840px;
    color: var(--count-text);
    font-weight: 700;
    font-size: 44px;
    line-height: 1;
    letter-spacing: 1px;
  }
</style>
</head>
<body>
  <main class="canvas">
    <section class="label">
      <svg class="label-shapes" width="913" height="950" viewBox="0 0 913 950" aria-hidden="true">
        <defs>
          <linearGradient id="band-gradient" x1="0" y1="0" x2="0" y2="1">
            <stop offset="0" stop-color="var(--band-blue-light)"/>
            <stop offset="1" stop-color="var(--band-blue)"/>
          </linearGradient>
        </defs>
        <path class="brand-panel" d="M0 0 H913 V312 H585 Q540 312 534 268 L528 96 Q525 54 488 54 H0 Z" fill="var(--panel-white)"/>
        <path class="brand-panel-edge" d="M0 56 H488 Q522 56 525 96 L531 268 Q537 318 585 318 H913" fill="none" stroke="var(--edge-green)" stroke-width="6"/>
        <path class="count-band" d="M0 811 H340 Q368 811 378 832 L392 858 Q398 866 414 866 H913 V950 H0 Z" fill="url(#band-gradient)"/>
      </svg>

      <div class="brand">
        <span class="brand-dot"></span>
        <span class="brand-name">Bright Even Wellness</span>
      </div>

      <h1 class="product-title">
        <span class="line-multi">Multi</span>
        <span class="line-vitamine">Vitamine</span>
      </h1>

      <div class="audience-pill">For women</div>

      <div class="capsule-count">30 Capsules</div>
    </section>
  </main>
</body>
</html>
```